Business Card Design for Kidvale (Hires out childrens play areas)

Looking to have a business card designed for a company we just bought. The company rents out childrens play areas.

I have uploaded a couple of examples of the kind of business card style I like. Here are two more examples:

https://quorvastudio.nz/project/bright-romp-branding/
https://imgvaultcdn.com/design_img/8841052/302917/302917_5518203_8841052_b73e19a2_image.jpg

I think a white card will be best due to all the colours in the logo.

Size we require: 3.75" x 2.25" (horizontally orientated) with a 0.125" bleed

Uploaded is two versions of our logo.

Details for the card:
1. My name: Liam Verster
2. Title: Managing Director
3. Phone no: 021 563 417
4. Email: liam@kidvale.co.nz
5. URL: www.kidvale.co.nz
6. Address:
PO Box 318625
Fernlea, Auckland

Let me know if you need anything else.

Target Market(s)

Hospitals, doctors surgeries, bed shops, etc.

Contact Information for Business Card

Details for the card:
1. My name: Liam Verster
3. Phone no: 021 563 417
5. URL: www.kidvale.co.nz
6. Address:
PO Box 318625
Fernlea, Auckland

Requirements
Should not have
• Not too busy.

```html
<!DOCTYPE html>
<html lang="en">
<head>
<meta charset="utf-8">
<title>Kidvale Business Card</title>
<link rel="stylesheet" href="https://fonts.googleapis.com/css2?family=Oswald:wght@500;600&family=Courier+Prime&display=swap">
<style>
  :root {
    --stage: #2c2e33;
    --card: #ececec;
    --ink: #111111;
    --brand: #1d4fa6;
    --name-box: #b8b8b8;
    --sky-light: #5ccaf5;
    --sky: #1e90e6;
    --sky-fill: #08aef0;
    --sun-orange: #ff9a00;
    --sun-amber: #ffb51a;
    --sun-yellow: #ffe100;
  }
  * { margin: 0; padding: 0; box-sizing: border-box; }
  html, body { width: 1200px; height: 900px; overflow: hidden; }
  body {
    background: var(--stage);
    display: flex;
    flex-direction: column;
    align-items: center;
    justify-content: center;
    gap: 36px;
    font-family: "Oswald", sans-serif;
  }
  .card {
    position: relative;
    width: 660px;
    height: 396px;
    background: var(--card);
    overflow: hidden;
    box-shadow: 0 6px 18px rgba(0,0,0,.35);
  }
  .card-waves { position: absolute; inset: 0; width: 100%; height: 100%; }
  .front-brand {
    position: absolute;
    left: 50%; top: 46%;
    transform: translate(-50%, -50%);
    display: flex; align-items: center; gap: 18px;
  }
  .brand-dot {
    width: 54px; height: 54px; border-radius: 50%;
    background: var(--brand);
  }
  .brand-name {
    font-weight: 600;
    font-size: 92px;
    line-height: 1;
    color: var(--brand);
  }
  /* back side */
  .card-back { display: flex; }
  .back-crease {
    position: absolute; inset: 0;
    background: linear-gradient(90deg, rgba(0,0,0,0) 44%, rgba(0,0,0,.10) 50%, rgba(255,255,255,.25) 51%, rgba(0,0,0,0) 60%);
  }
  .identity {
    position: relative;
    width: 50%;
    padding: 70px 0 0 44px;
  }
  .identity .brand-mini {
    display: flex; align-items: center; gap: 10px;
    margin-left: 96px; margin-bottom: 20px;
  }
  .identity .brand-dot { width: 26px; height: 26px; }
  .identity .brand-name { font-size: 44px; }
  .person-name {
    display: inline-block;
    background: var(--name-box);
    color: var(--ink);
    font-weight: 500;
    font-size: 40px;
    line-height: 1;
    padding: 8px 14px 10px;
  }
  .person-title {
    font-family: "Courier Prime", monospace;
    font-size: 15px;
    letter-spacing: 1px;
    color: #333333;
    margin: 10px 0 0 14px;
  }
  .contact-list {
    position: relative;
    width: 50%;
    list-style: none;
    padding: 92px 0 0 34px;
  }
  .contact-item {
    display: flex; align-items: flex-start; gap: 18px;
    font-weight: 500;
    font-size: 24px;
    line-height: 1.2;
    color: var(--ink);
    margin-bottom: 12px;
  }
  .contact-icon { width: 24px; height: 24px; flex: none; margin-top: 3px; fill: var(--ink); }
</style>
</head>
<body>

  <section class="card card-front" aria-label="Card front">
    <svg class="card-waves" viewBox="0 0 660 396" preserveAspectRatio="none" aria-hidden="true">
      <path d="M250,0 C400,30 560,130 660,330 L660,0 Z" fill="var(--sun-amber)"/>
      <path d="M290,0 C430,35 580,140 660,300 L660,0 Z" fill="var(--sun-orange)"/>
      <path d="M310,0 C445,40 590,150 660,285 L660,0 Z" fill="var(--sun-amber)"/>
      <path d="M340,0 C470,45 600,160 660,270 L660,0 Z" fill="var(--sun-yellow)"/>
      <path d="M0,108 C160,140 310,240 400,396 L0,396 Z" fill="var(--sky-light)"/>
      <path d="M0,128 C150,160 290,255 370,396 L0,396 Z" fill="var(--sky)"/>
      <path d="M0,146 C140,178 270,268 345,396 L0,396 Z" fill="var(--sky-fill)"/>
      <path d="M0,170 C130,205 250,285 315,396 L0,396 Z" fill="var(--sky)"/>
      <path d="M0,188 C120,224 232,300 292,396 L0,396 Z" fill="var(--sky-fill)"/>
    </svg>
    <div class="front-brand">
      <span class="brand-dot"></span>
      <span class="brand-name">Kidvale</span>
    </div>
  </section>

  <section class="card card-back" aria-label="Card back">
    <div class="back-crease"></div>
    <div class="identity">
      <div class="brand-mini">
        <span class="brand-dot"></span>
        <span class="brand-name">Kidvale</span>
      </div>
      <div class="person-name">Liam Verster</div>
      <p class="person-title">Managing Director</p>
    </div>
    <ul class="contact-list">
      <li class="contact-item">
        <svg class="contact-icon" viewBox="0 0 24 24"><path d="M6.6 10.8a15 15 0 0 0 6.6 6.6l2.2-2.2c.3-.3.7-.4 1-.2 1.1.4 2.3.6 3.6.6.6 0 1 .4 1 1V20c0 .6-.4 1-1 1C10.6 21 3 13.4 3 4c0-.6.4-1 1-1h3.5c.6 0 1 .4 1 1 0 1.3.2 2.5.6 3.6.1.3 0 .7-.2 1z"/></svg>
        <span>021 563 417</span>
      </li>
      <li class="contact-item">
        <svg class="contact-icon" viewBox="0 0 24 24"><path d="M12 2a7 7 0 0 0-7 7c0 5 7 13 7 13s7-8 7-13a7 7 0 0 0-7-7zm0 9.5A2.5 2.5 0 1 1 12 6.5a2.5 2.5 0 0 1 0 5z"/></svg>
        <span>liam@kidvale.co.nz</span>
      </li>
      <li class="contact-item">
        <svg class="contact-icon" viewBox="0 0 24 24"><circle cx="10" cy="10" r="6" fill="none" stroke="#111" stroke-width="2.4"/><path d="M14.5 14.5 21 21" stroke="#111" stroke-width="2.8" stroke-linecap="round"/></svg>
        <span>www.kidvale.co.nz</span>
      </li>
      <li class="contact-item">
        <svg class="contact-icon" viewBox="0 0 24 24"><path d="M2 5h20v14H2z"/><path d="M2 5l10 8 10-8" fill="none" stroke="#ececec" stroke-width="1.6"/></svg>
        <span>PO Box 318625<br>Fernlea, Auckland</span>
      </li>
    </ul>
  </section>

</body>
</html>
```